Machine shop needs a brochure designed

Would like a tri-fold professional looking brochure that tells about our business and our capabilities. We are a family-owned business with over 50 years of experience in precision manufacturing. We specialize in close-tolerance tooling and serve a diverse array of industries. Our colors are red, black, white, and gray. The final design should make a great impression and spotlight our capabilities and quality.

Target Market(s)

Manufacturing industries needing tooling

Industry/Entity Type

Machining, grinding, manufacturing

Font styles to use
Serif

Colors
EB3D1F
EC4F4E
F09395
F8D3D4
FCEDEE

Requirements
Must have
• Logo, colors are red, black, white, gray
Nice to have
• Images of CNC process or machining/grinding metal parts.

```html
<!DOCTYPE html>
<html lang="en">
<head>
<meta charset="utf-8">
<title>Kestrel Industries, Inc. — Tri-fold Brochure</title>
<link href="https://fonts.googleapis.com/css2?family=Montserrat:ital,wght@0,400;0,500;0,600;0,700;0,800;0,900;1,700&display=swap" rel="stylesheet">
<style>
  :root {
    --red: #dd1c28;
    --red-deep: #c8151f;
    --ink: #231f20;
    --paper: #ffffff;
    --paper-gray: #efefef;
    --backdrop: #cfcfcf;
    --steel-light: #d7dbe0;
    --steel-dark: #5d6670;
    --photo-rose: #a9898c;
  }
  * { box-sizing: border-box; margin: 0; padding: 0; }
  html, body { width: 814px; height: 1200px; overflow: hidden; }
  body {
    background: var(--backdrop);
    font-family: "Montserrat", Arial, sans-serif;
    color: var(--ink);
    position: relative;
  }
  .spread {
    position: absolute;
    left: 137px;
    width: 540px;
    height: 398px;
    overflow: hidden;
    box-shadow: 0 2px 6px rgba(0,0,0,.18);
  }
  .spread--outside { top: 100px; }
  .spread--inside { top: 700px; }
  .abs { position: absolute; }
  .spread-bg { position: absolute; inset: 0; }

  .heading {
    font-weight: 800;
    color: var(--red);
    font-size: 11.5px;
    line-height: 1.15;
  }
  .rule { position: absolute; width: 28px; height: 1.5px; background: var(--ink); }
  .rule--light { background: var(--ink); }
  .body-copy { font-size: 6.6px; line-height: 1.36; font-weight: 500; }
  .body-copy p + p { margin-top: 6px; }

  /* outside: quality panel */
  .qa-title { left: 17px; top: 19px; width: 160px; }
  .qa-copy { left: 17px; top: 72px; width: 130px; }
  .qa-quote {
    left: 31px; top: 316px; width: 125px;
    color: var(--paper); font-style: italic; font-weight: 700;
    font-size: 7.1px; line-height: 1.3;
  }
  .qa-quote-bar { left: 17px; top: 314px; width: 1.5px; height: 78px; background: var(--ink); }

  /* outside: contact panel */
  .contact { left: 180px; width: 180px; text-align: center; }
  .contact-title { top: 16px; font-size: 11.5px; }
  .contact-intro { top: 46px; padding: 0 18px; font-size: 6.6px; line-height: 1.36; font-weight: 500; }
  .contact-name { top: 122px; }
  .contact-name .big { font-size: 15.5px; font-weight: 900; line-height: 1; display: block; }
  .contact-name .small { font-size: 10px; font-weight: 800; display: block; margin-top: 2px; }
  .contact-list { top: 253px; color: var(--paper); font-size: 6.9px; font-weight: 700; line-height: 1.4; }
  .contact-item { display: flex; flex-direction: column; align-items: center; margin-bottom: 6px; }
  .contact-item svg { width: 9px; height: 9px; margin-bottom: 2px; }

  .wordmark {
    display: flex; align-items: center; justify-content: center; gap: 4px;
    font-weight: 800; color: var(--red); font-size: 10px; letter-spacing: .06em;
  }
  .wordmark .mark { width: 9px; height: 9px; background: var(--red); }

  /* outside: cover panel */
  .cover { left: 360px; width: 180px; text-align: center; }
  .cover-wordmark { top: 44px; }
  .cover-title { top: 86px; font-size: 18px; font-weight: 900; line-height: 1.13; }
  .cover-tagline { top: 314px; color: var(--paper); font-size: 10px; font-weight: 700; line-height: 1.3; padding: 0 8px; }
  .cover-web {
    left: 394px; top: 372px; width: 112px; height: 16px; background: var(--paper);
    font-size: 6.8px; font-weight: 700; text-align: center; line-height: 16px;
  }

  /* inside */
  .welcome-title { left: 17px; top: 12px; color: var(--paper); font-size: 11.5px; }
  .welcome-copy { left: 17px; top: 63px; width: 150px; color: var(--paper); font-size: 6.9px; line-height: 1.33; font-weight: 500; }
  .about-title { left: 199px; top: 126px; font-size: 11.5px; }
  .about-copy { left: 199px; top: 160px; width: 146px; font-size: 6.4px; line-height: 1.33; }
  .cap-title { left: 378px; top: 127px; font-size: 11.5px; }
  .cap-copy { left: 378px; top: 160px; width: 138px; font-size: 6.8px; line-height: 1.35; font-weight: 500; }
  .cap-copy h3 { font-size: 7.4px; font-weight: 700; margin: 5px 0 2px; }
  .cap-list { list-style: none; font-size: 6.2px; line-height: 1.3; }
  .cap-list li { position: relative; padding-left: 10px; margin-bottom: 2.2px; }
  .cap-list li::before {
    content: ""; position: absolute; left: 1px; top: 2.6px;
    width: 2.4px; height: 2.4px; border-radius: 50%; background: var(--red);
  }
</style>
</head>
<body>

<!-- Outside of the brochure -->
<section class="spread spread--outside">
  <svg class="spread-bg" viewBox="0 0 540 398" width="540" height="398" aria-hidden="true">
    <rect x="0" y="0" width="180" height="398" fill="var(--paper)"/>
    <rect x="180" y="0" width="180" height="398" fill="var(--paper-gray)"/>
    <rect x="360" y="0" width="180" height="398" fill="var(--paper-gray)"/>
    <rect x="360" y="0" width="180" height="12" fill="var(--ink)"/>
    <polygon points="0,297 180,255 360,207 540,262 540,398 0,398" fill="var(--red)"/>
    <polyline points="0,297 180,255 360,207 540,262" fill="none" stroke="var(--ink)" stroke-width="4"/>
    <line x1="180" y1="0" x2="180" y2="398" stroke="rgba(0,0,0,.06)" stroke-width="1"/>
    <line x1="360" y1="0" x2="360" y2="398" stroke="rgba(0,0,0,.08)" stroke-width="1"/>
    <circle cx="450" cy="238" r="66" fill="var(--ink)"/>
    <defs>
      <radialGradient id="bottling-line" cx="50%" cy="45%" r="60%">
        <stop offset="0" stop-color="var(--steel-light)"/>
        <stop offset="1" stop-color="var(--steel-dark)"/>
      </radialGradient>
    </defs>
    <circle cx="450" cy="238" r="59" fill="url(#bottling-line)" role="img" aria-label="Photo of a production line with metal cans on a conveyor"/>
  </svg>

  <h2 class="abs heading qa-title">Kestrel Industries<br>Quality Assurance</h2>
  <div class="rule" style="left:17px; top:54px;"></div>
  <div class="abs body-copy qa-copy">
    <p>Kestrel Industries, Inc. is committed to quality and consistency. We are constantly striving to implement new ways to adhere to a high mark while providing our clients with their orders in as short a time frame as possible. It is not only our goal, but we understand it to be our responsibility to provide our clients with the highest quality products.</p>
    <p>The inspection process at Kestrel Industries, Inc. begins immediately upon receipt of our materials. All materials are inspected to ensure consistency and are re-inspected throughout the entire process, right up to shipping. We inspect 100% of our parts and catalog all of our orders prior to shipment. We have our own written Quality Assurance program that is specific to our operations and available upon request.</p>
  </div>
  <div class="abs qa-quote-bar"></div>
  <p class="abs qa-quote">We welcome the opportunity to quote your project, and with 40 years combined experience in precision manufacturing, you can rest assured that jobs placed with us will be done to your satisfaction, every time.</p>

  <h2 class="abs heading contact contact-title">Contact Us</h2>
  <div class="rule" style="left:256px; top:36px;"></div>
  <p class="abs contact contact-intro">We welcome the opportunity to quote your project, and with 40 years combined experience in precision manufacturing, you can rest assured that jobs placed with us will be done to your satisfaction, every time.</p>
  <div class="abs contact contact-name">
    <span class="big">KESTREL</span>
    <span class="small">INDUSTRIES, INC.</span>
  </div>
  <div class="abs contact wordmark" style="top:175px;"><span class="mark"></span>KESTREL</div>

  <div class="abs contact contact-list">
    <div class="contact-item">
      <svg viewBox="0 0 10 10"><circle cx="5" cy="5" r="5" fill="#fff"/><path d="M5 2.2a1.8 1.8 0 0 1 1.8 1.8C6.8 5.3 5 7.6 5 7.6S3.2 5.3 3.2 4A1.8 1.8 0 0 1 5 2.2z" fill="var(--red)"/><circle cx="5" cy="4" r=".7" fill="#fff"/></svg>
      <span>1450 Harlow Mill Road<br>Fairview, TN 37062</span>
    </div>
    <div class="contact-item">
      <svg viewBox="0 0 10 10"><circle cx="5" cy="5" r="5" fill="#fff"/><path d="M3.2 2.4l1.1 1.4-.6.8c.4.8 1 1.4 1.8 1.8l.8-.6 1.4 1.1-.6 1c-2.4-.2-4.4-2.2-4.6-4.6z" fill="var(--red)"/></svg>
      <span>555-014-2200</span>
    </div>
    <div class="contact-item">
      <svg viewBox="0 0 10 10"><circle cx="5" cy="5" r="5" fill="#fff"/><rect x="3.4" y="2.3" width="3.2" height="1.8" fill="var(--red)"/><rect x="2.4" y="4.2" width="5.2" height="2.4" fill="var(--red)"/><rect x="3.4" y="6" width="3.2" height="1.6" fill="var(--red)"/></svg>
      <span>555-014-2201</span>
    </div>
    <div class="contact-item">
      <svg viewBox="0 0 10 10"><circle cx="5" cy="5" r="5" fill="#fff"/><rect x="2.4" y="3.2" width="5.2" height="3.6" fill="var(--red)"/><path d="M2.6 3.4L5 5.3l2.4-1.9" fill="none" stroke="#fff" stroke-width=".5"/></svg>
      <span>quotes@kestrelindustries.net</span>
    </div>
    <div class="contact-item">
      <svg viewBox="0 0 10 10"><circle cx="5" cy="5" r="5" fill="#fff"/><circle cx="5" cy="5" r="2.6" fill="none" stroke="var(--red)" stroke-width=".6"/><ellipse cx="5" cy="5" rx="1.1" ry="2.6" fill="none" stroke="var(--red)" stroke-width=".5"/><line x1="2.4" y1="5" x2="7.6" y2="5" stroke="var(--red)" stroke-width=".5"/></svg>
      <span>www.kestrelindustries.net</span>
    </div>
  </div>

  <div class="abs cover wordmark cover-wordmark" style="font-size:12px;"><span class="mark" style="width:11px;height:11px;"></span>KESTREL</div>
  <h1 class="abs cover cover-title">KESTREL<br>INDUSTRIES,<br>INC.</h1>
  <p class="abs cover cover-tagline">Precision Manufacturing, Machining, Grinding and Innovations.</p>
  <div class="abs cover-web">www.kestrelindustries.net</div>
</section>

<!-- Inside of the brochure -->
<section class="spread spread--inside">
  <svg class="spread-bg" viewBox="0 0 540 398" width="540" height="398" aria-hidden="true">
    <defs>
      <linearGradient id="metal-stock" x1="0" y1="0" x2="1" y2="1">
        <stop offset="0" stop-color="#e4e7ea"/>
        <stop offset=".5" stop-color="#9aa2ab"/>
        <stop offset="1" stop-color="#d2d6da"/>
      </linearGradient>
      <linearGradient id="machine-hall" x1="0" y1="0" x2="1" y2="1">
        <stop offset="0" stop-color="#c9b2b4"/>
        <stop offset="1" stop-color="#4a3436"/>
      </linearGradient>
    </defs>
    <rect x="0" y="0" width="180" height="398" fill="var(--red)"/>
    <rect x="180" y="0" width="180" height="398" fill="var(--paper-gray)"/>
    <rect x="360" y="0" width="180" height="398" fill="var(--paper)"/>
    <rect x="522" y="218" width="18" height="180" fill="var(--red)"/>
    <rect x="180" y="0" width="33" height="76" fill="var(--ink)"/>
    <rect x="198" y="0" width="342" height="113" fill="url(#metal-stock)" role="img" aria-label="Photo of stacked aluminium bars, tubes and profiles"/>
    <rect x="17" y="158" width="163" height="205" fill="var(--ink)"/>
    <rect x="0" y="184" width="163" height="156" fill="url(#machine-hall)" role="img" aria-label="Photo of a CNC machine inside a workshop"/>
    <line x1="360" y1="113" x2="360" y2="398" stroke="rgba(0,0,0,.07)" stroke-width="1"/>
  </svg>

  <h2 class="abs heading welcome-title">Welcome to Kestrel<br>Industries, Inc.</h2>
  <div class="rule" style="left:17px; top:46px;"></div>
  <p class="abs welcome-copy">When your project or process requires precise, high-quality parts or components, look no further than Kestrel. We welcome the opportunity to quote your project, and with 40 years combined experience in precision manufacturing, you can rest assured that jobs placed with us will be done to your satisfaction, every time.</p>

  <h2 class="abs heading about-title">About Us</h2>
  <div class="abs body-copy about-copy">
    <p>Kestrel Industries, Inc. is a privately owned company with over fifty years of experience in precision manufacturing. Products manufactured include components for the Sentinel missile during Operation Desert Storm, machine gun barrels, close tolerance can tooling, conveyor slats and rollers, molds, various production tooling for several national industries, pump housings for the gasoline industry, aviation and automotive manufacturing, and various precision machining and grinding jobs.</p>
    <p>We at Kestrel Industries, Inc. look forward to the opportunity to work with you and quote any projects you might want us to look at. We take a “Quality first” approach to all of our jobs and we have the determination to get the job done according to our clients’ timelines. We are always looking for opportunities to form new alliances and friendships with prospective clients.</p>
  </div>

  <h2 class="abs heading cap-title">Capabilities</h2>
  <div class="rule" style="left:378px; top:145px;"></div>
  <div class="abs cap-copy">
    <p>We at Kestrel offer a wide variety of services to meet your machining and tooling needs.</p>
    <h3>Our capabilities include:</h3>
    <ul class="cap-list">
      <li>Soft cutting</li>
      <li>Hard cutting</li>
      <li>CNC Machining</li>
      <li>CNC Milling</li>
      <li>Grinding- O.D./ I.D. and Surface/Rotary (Carbide, Steel, etc.)</li>
      <li>0-2 Micro-finishing</li>
      <li>Light fabrication</li>
      <li>Conveyor assemblies - slats, rollers, etc.</li>
      <li>Can tooling- Trimmer Knives, Knockouts, Punch Bolts, Printer Mandrels, Cut Edges, Blank and Draw Dies, etc.</li>
      <li>Wide range of Aerospace and Automotive tooling</li>
      <li>NAICS 332813, 332721 &amp; 333512</li>
    </ul>
  </div>
</section>

</body>
</html>
```